Vantor Ridge needs a Business Card Design

We need a business card design for an Information Technology company based in Fairfax Virginia called Vantor Ridge. We want the business card to use our logo colors. We need it to be double-sided. The business card needs to look professional but we would like it to be unique. You can get company information from our web site (http://www.vantorridgellc.example).

Target Market(s)

Target market is Government Agencies and Business Professionals.

Industry/Entity Type

Business

Requirements
Must have
• Must have section for company name, company address, company URL, employee name, title, phone and email. Also must have company logo and space for entering logos.

```html
<!DOCTYPE html>
<html lang="en">
<head>
<meta charset="utf-8">
<title>Vantor Ridge — Business Card</title>
<link href="https://fonts.googleapis.com/css2?family=Open+Sans:wght@400;600;700&display=swap" rel="stylesheet">
<style>
  :root {
    --navy: #1f2f86;
    --navy-deep: #17226a;
    --royal: #2b3f9e;
    --sky: #0a78c0;
    --line: #3c8fd6;
    --paper: #ffffff;
    --backdrop: #e9e6e1;
    --ink-soft: #dfe6ff;
    --icon: #6fb3ff;
  }
  * { box-sizing: border-box; margin: 0; padding: 0; }
  html, body { width: 1200px; height: 1024px; overflow: hidden; }
  body {
    background: var(--backdrop);
    font-family: "Open Sans", Arial, sans-serif;
    position: relative;
  }
  .card {
    position: absolute;
    width: 640px;
    height: 366px;
    background: var(--paper);
    box-shadow: 0 10px 28px rgba(0,0,0,0.22);
    overflow: hidden;
  }
  /* Front */
  .card-front { left: 280px; top: 110px; }
  .front-brand {
    position: absolute; left: 0; top: 0; width: 100%; height: 196px;
    display: flex; align-items: center; padding-left: 92px; gap: 16px;
  }
  .brand-mark { width: 40px; height: 40px; background: var(--navy); }
  .brand-name {
    font-weight: 700; font-size: 40px; color: var(--navy);
    text-transform: uppercase; letter-spacing: 0.5px; white-space: nowrap;
  }
  .front-divider {
    position: absolute; left: 0; top: 196px; width: 100%; height: 4px;
    background: var(--line);
  }
  .front-panel {
    position: absolute; left: 0; top: 200px; width: 100%; height: 166px;
    background: linear-gradient(100deg, var(--navy-deep) 0%, var(--royal) 55%, var(--navy) 100%);
    color: var(--paper);
  }
  .person { position: absolute; left: 24px; bottom: 20px; }
  .person-name { font-weight: 700; font-size: 19px; }
  .person-title { font-size: 14px; color: var(--ink-soft); margin-top: 2px; padding-left: 60px; }
  .panel-rule {
    position: absolute; left: 360px; top: 20px; width: 1px; height: 126px;
    background: linear-gradient(transparent, rgba(255,255,255,0.55), transparent);
  }
  .contact {
    position: absolute; left: 384px; top: 18px;
    font-size: 13.5px; line-height: 19px; list-style: none; white-space: nowrap;
  }
  .contact li { display: flex; align-items: flex-start; gap: 8px; }
  .contact li.gap { margin-top: 8px; }
  .contact svg { flex: none; margin-top: 3px; }
  .contact .indent { padding-left: 20px; }
  /* Back */
  .card-back { left: 280px; top: 548px; }
  .back-band {
    position: absolute; left: 0; top: 0; width: 100%; height: 150px;
    background: var(--sky);
  }
  .back-band-top {
    position: absolute; left: 0; top: 0; width: 100%; height: 46px;
    background: var(--royal);
  }
  .back-brand {
    position: absolute; right: 34px; top: 186px;
    display: flex; align-items: center; gap: 12px;
  }
  .back-brand .brand-mark { width: 30px; height: 30px; }
  .back-brand .brand-name { font-size: 32px; }
  .url-strip {
    position: absolute; left: 0; bottom: 0; width: 300px; height: 46px;
    background: var(--sky);
    clip-path: polygon(0 0, 92% 0, 100% 100%, 0 100%);
    color: var(--paper); font-size: 14px; white-space: nowrap;
    display: flex; align-items: center; padding-left: 32px;
  }
</style>
</head>
<body>

<section class="card card-front" aria-label="Business card front">
  <div class="front-brand">
    <span class="brand-mark"></span>
    <span class="brand-name">Vantor Ridge</span>
  </div>
  <div class="front-divider"></div>
  <div class="front-panel">
    <div class="person">
      <p class="person-name">Daniel Morrow</p>
      <p class="person-title">Job Title</p>
    </div>
    <div class="panel-rule"></div>
    <ul class="contact">
      <li>
        <svg width="12" height="12" viewBox="0 0 12 12"><path d="M6 0C3.8 0 2 1.8 2 4c0 3 4 8 4 8s4-5 4-8c0-2.2-1.8-4-4-4zm0 5.5A1.5 1.5 0 1 1 6 2.5a1.5 1.5 0 0 1 0 3z" fill="var(--icon)"/></svg>
        <span>4410 Larkspur Way, Suite 300</span>
      </li>
      <li class="indent">Alder Falls, OR 97401</li>
      <li class="gap">
        <svg width="12" height="12" viewBox="0 0 12 12"><path d="M2.5 0.5l2 2.2-1 1.3c.8 1.6 2 2.8 3.5 3.5l1.3-1 2.2 2-1 2c-4.5-.3-8.7-4.5-9-9z" fill="var(--icon)"/></svg>
        <span>877.555.0142</span>
      </li>
      <li>
        <svg width="12" height="12" viewBox="0 0 12 12"><rect x="2" y="0.5" width="8" height="4" fill="var(--icon)"/><rect x="0.5" y="4.5" width="11" height="5" rx="1" fill="var(--icon)"/><rect x="2.5" y="8" width="7" height="3.5" fill="#ffffff"/></svg>
        <span>888.555.0187</span>
      </li>
      <li>
        <svg width="12" height="12" viewBox="0 0 12 12"><rect x="0.5" y="2" width="11" height="8" fill="var(--icon)"/><path d="M0.5 2l5.5 4.5L11.5 2" stroke="#1f2f86" stroke-width="1" fill="none"/></svg>
        <span>name@vantorridge.example</span>
      </li>
      <li>
        <svg width="12" height="12" viewBox="0 0 12 12"><circle cx="6" cy="6" r="5.5" fill="var(--icon)"/><path d="M0.5 6h11M6 0.5c-2.5 3-2.5 8 0 11M6 0.5c2.5 3 2.5 8 0 11" stroke="#1f2f86" stroke-width="0.8" fill="none"/></svg>
        <span>www.vantorridgellc.example</span>
      </li>
    </ul>
  </div>
</section>

<section class="card card-back" aria-label="Business card back">
  <div class="back-band"></div>
  <div class="back-band-top"></div>
  <div class="back-brand">
    <span class="brand-mark"></span>
    <span class="brand-name">Vantor Ridge</span>
  </div>
  <div class="url-strip">www.vantorridgellc.example</div>
</section>

</body>
</html>
```